Beautiful e-comm site for 'roadside farmers stand' online!

Need a logo design and basic e-comm website (super super simple) for new business called Brindlecove. Brindlecove is an online farmers stand where local artisans can sell 'brindlecove' goods directly from their makers!

Looking for something simple, whimsicle and clean! (Ideally with a light grey or perrywinkle and some color mixed in - word 'Brindlecove' in black - can work the pear shape in somewhere but not required!)

Target Market(s)

Hobby shoppers and 'quilo' goers who want a focus on edible things and care about ingredients!

Industry/Entity Type

E-Commerce

Number of Pages Required

2 page

Font styles to use
Decorative
Script

Colors
f3f1f8
ec1f27
cadf82

Requirements
Must have
• - Basic logo
• - Homepage
• - Product Detail Page
• - Be in a responsive, woocommerce or shopify, wordpress theme (will purchase theme after design is approved)
Nice to have
• - Matching check out & cart pages
• - 'About Us' page
• - SEO plugin
Should not have
• A cluttered look/feel.

```html
<!DOCTYPE html>
<html lang="en">
<head>
<meta charset="utf-8">
<title>Brindlecove – Reviews &amp; Footer</title>
<link href="https://fonts.googleapis.com/css2?family=Poppins:wght@400;500;600&display=swap" rel="stylesheet">
<style>
  :root{
    --ink:#2b2b33;
    --muted:#9aa3b5;
    --soft:#b6bccb;
    --line:#e6e8ee;
    --verified:#3cb44b;
    --heart:#f44a4a;
    --star:#f5c400;
    --link-blue:#4a7fd6;
    --footer:#2e2f35;
    --footer-text:#c9cbd2;
    --footer-dim:#7d8089;
    --badge:#5a5c63;
    --tweet:#1d8cf8;
    --page:#ffffff;
  }
  *{box-sizing:border-box;margin:0;padding:0}
  html,body{width:1200px;height:1200px;overflow:hidden;background:var(--page)}
  body{font-family:'Poppins',sans-serif;color:var(--ink)}
  .stage{position:absolute;left:0;top:0;width:1415px;height:1415px;transform:scale(0.848);transform-origin:0 0}
  .abs{position:absolute}

  .actions{display:flex;align-items:center;gap:24px;font-size:9px;color:var(--muted);white-space:nowrap}
  .actions span{display:flex;align-items:center;gap:6px}
  .actions .helpful{color:var(--ink)}
  .avatar{width:30px;height:30px;border-radius:50%;background:#f1f2f6}
  .name{font-size:11px;font-weight:500;white-space:nowrap}
  .name small{font-size:9px;color:var(--soft);font-weight:400;margin-left:4px}
  .verified{font-size:9px;color:var(--verified);font-weight:500;white-space:nowrap}
  .stars{display:flex;align-items:center;gap:2px;font-size:11px;white-space:nowrap}
  .stars svg{width:9px;height:9px}
  .stars b{font-weight:400;margin-left:10px}
  .body-text{font-size:9px;line-height:15px;width:495px;color:#4a4f5c}
  .found{font-size:9px;color:var(--muted);white-space:nowrap}
  .rule{height:1px;background:var(--line)}

  .pager{font-size:9px;color:var(--muted);letter-spacing:.3px;white-space:nowrap}
  .pager.nav{display:flex;align-items:center;gap:6px;font-size:10px}
  .pager.pages{color:var(--link-blue);font-size:9px;word-spacing:3px}

  .section-title{font-size:13px;font-weight:500;width:300px;text-align:center;margin-left:-150px}
  .thumb{width:146px;height:146px}
  .overlay{position:absolute;left:0;bottom:0;width:100%;height:28px;background:rgba(30,30,34,.85);display:flex;align-items:center;justify-content:flex-end;padding-right:8px;font-size:8px;color:#fff;font-weight:500}
  .overlay i{position:absolute;left:0;top:0;width:28px;height:28px;background:var(--heart);display:flex;align-items:center;justify-content:center}

  .footer{left:0;top:904px;width:1415px;height:511px;background:var(--footer);color:var(--footer-text)}
  .col h4{font-size:9px;font-weight:600;color:#fff;letter-spacing:.3px;margin-bottom:17px;white-space:nowrap}
  .col ul{list-style:none;font-size:10px;line-height:22px;white-space:nowrap}
  .col p{font-size:8px;color:var(--footer-dim);line-height:14px;white-space:nowrap}
  .col p b{color:var(--footer-text);font-weight:400}
  .newsletter-box{width:248px;height:30px;border:1px solid #3d3e45;border-radius:15px;display:flex;align-items:center;justify-content:space-between;padding:0 14px 0 22px;font-size:10px;color:#fff;white-space:nowrap}
  .payments{left:0;width:1415px;top:252px;display:flex;justify-content:center;gap:44px}
  .pay{display:flex;align-items:center;gap:8px;font-size:14px;font-weight:500;color:var(--badge);white-space:nowrap}
  .pay i{width:10px;height:10px;border-radius:50%;background:var(--badge)}
  .social{width:12px;height:12px;border-radius:50%;background:#55575e;margin:-6px 0 0 -6px}
  .social.active{width:28px;height:28px;margin:-14px 0 0 -14px;background:var(--tweet);box-shadow:0 4px 12px rgba(29,140,248,.5)}
  .brand{font-size:28px;font-weight:500;color:#fff;width:300px;text-align:center;margin-left:-150px}
</style>
</head>
<body>
<div class="stage">

  <div class="abs actions" style="left:113px;top:12px">
    <span class="helpful"><svg width="13" height="12" viewBox="0 0 24 22"><path d="M12 21 2.5 11.5A5.5 5.5 0 0 1 12 4a5.5 5.5 0 0 1 9.5 7.5Z" fill="#f44a4a"/></svg>Helpful</span>
    <span><svg width="12" height="11" viewBox="0 0 24 22"><path d="M3 4h18v12H9l-5 4v-4H3z" fill="none" stroke="#9aa3b5" stroke-width="2"/></svg>200 comments</span>
    <span>Report abuse</span>
  </div>

  <div class="abs avatar" style="left:112px;top:62px"></div>
  <div class="abs name" style="left:169px;top:63px">Michael<small>15 hours ago</small></div>
  <div class="abs verified" style="left:589px;top:65px">Verified Purchased</div>
  <div class="abs stars" style="left:169px;top:87px">
    <svg viewBox="0 0 10 10"><path d="M5 0l1.5 3.2 3.5.4-2.6 2.4.7 3.5L5 7.8 1.9 9.5l.7-3.5L0 3.6l3.5-.4z" fill="#f5c400"/></svg><svg viewBox="0 0 10 10"><path d="M5 0l1.5 3.2 3.5.4-2.6 2.4.7 3.5L5 7.8 1.9 9.5l.7-3.5L0 3.6l3.5-.4z" fill="#f5c400"/></svg><svg viewBox="0 0 10 10"><path d="M5 0l1.5 3.2 3.5.4-2.6 2.4.7 3.5L5 7.8 1.9 9.5l.7-3.5L0 3.6l3.5-.4z" fill="#f5c400"/></svg><svg viewBox="0 0 10 10"><path d="M5 0l1.5 3.2 3.5.4-2.6 2.4.7 3.5L5 7.8 1.9 9.5l.7-3.5L0 3.6l3.5-.4z" fill="#f5c400"/></svg><svg viewBox="0 0 10 10"><path d="M5 0l1.5 3.2 3.5.4-2.6 2.4.7 3.5L5 7.8 1.9 9.5l.7-3.5L0 3.6l3.5-.4z" fill="#f5c400"/></svg>
    <b>This is &nbsp;a must buy!</b>
  </div>
  <p class="abs body-text" style="left:169px;top:108px">Lorem ipsum dolor sit amet, consectetur adipisicing elit, sed do eiusmod tempor incididunt ut labore et dolore magna aliqua. Ut enim ad minim veniam,</p>
  <div class="abs found" style="left:113px;top:156px">120 people found this helpful</div>
  <div class="abs actions" style="left:113px;top:182px">
    <span class="helpful"><svg width="13" height="12" viewBox="0 0 24 22"><path d="M12 21 2.5 11.5A5.5 5.5 0 0 1 12 4a5.5 5.5 0 0 1 9.5 7.5Z" fill="#f44a4a"/></svg>Helpful</span>
    <span><svg width="12" height="11" viewBox="0 0 24 22"><path d="M3 4h18v12H9l-5 4v-4H3z" fill="none" stroke="#9aa3b5" stroke-width="2"/></svg>200 comments</span>
    <span>Report abuse</span>
  </div>

  <div class="abs avatar" style="left:112px;top:232px"></div>
  <div class="abs name" style="left:169px;top:233px">Michael<small>15 hours ago</small></div>
  <div class="abs verified" style="left:589px;top:235px">Verified Purchased</div>
  <div class="abs stars" style="left:169px;top:257px">
    <svg viewBox="0 0 10 10"><path d="M5 0l1.5 3.2 3.5.4-2.6 2.4.7 3.5L5 7.8 1.9 9.5l.7-3.5L0 3.6l3.5-.4z" fill="#f5c400"/></svg><svg viewBox="0 0 10 10"><path d="M5 0l1.5 3.2 3.5.4-2.6 2.4.7 3.5L5 7.8 1.9 9.5l.7-3.5L0 3.6l3.5-.4z" fill="#f5c400"/></svg><svg viewBox="0 0 10 10"><path d="M5 0l1.5 3.2 3.5.4-2.6 2.4.7 3.5L5 7.8 1.9 9.5l.7-3.5L0 3.6l3.5-.4z" fill="#f5c400"/></svg><svg viewBox="0 0 10 10"><path d="M5 0l1.5 3.2 3.5.4-2.6 2.4.7 3.5L5 7.8 1.9 9.5l.7-3.5L0 3.6l3.5-.4z" fill="#f5c400"/></svg><svg viewBox="0 0 10 10"><path d="M5 0l1.5 3.2 3.5.4-2.6 2.4.7 3.5L5 7.8 1.9 9.5l.7-3.5L0 3.6l3.5-.4z" fill="#f5c400"/></svg>
    <b>This is &nbsp;a must buy!</b>
  </div>
  <p class="abs body-text" style="left:169px;top:278px">Lorem ipsum dolor sit amet, consectetur adipisicing elit, sed do eiusmod tempor incididunt ut labore et dolore magna aliqua. Ut enim ad minim veniam,</p>
  <div class="abs found" style="left:113px;top:326px">120 people found this helpful</div>
  <div class="abs actions" style="left:113px;top:352px">
    <span class="helpful"><svg width="13" height="12" viewBox="0 0 24 22"><path d="M12 21 2.5 11.5A5.5 5.5 0 0 1 12 4a5.5 5.5 0 0 1 9.5 7.5Z" fill="#f44a4a"/></svg>Helpful</span>
    <span><svg width="12" height="11" viewBox="0 0 24 22"><path d="M3 4h18v12H9l-5 4v-4H3z" fill="none" stroke="#9aa3b5" stroke-width="2"/></svg>200 comments</span>
    <span>Report abuse</span>
  </div>

  <div class="abs rule" style="left:113px;top:412px;width:561px"></div>

  <div class="abs pager" style="left:113px;top:437px">PAGE &nbsp;1 OF 30</div>
  <div class="abs pager nav" style="left:503px;top:436px">
    <svg width="7" height="10" viewBox="0 0 7 10"><path d="M6 1 2 5l4 4" fill="none" stroke="#9aa3b5" stroke-width="1.3"/></svg>PREV
  </div>
  <div class="abs pager pages" style="left:560px;top:438px">1 2 3 4 .. 30</div>
  <div class="abs pager nav" style="left:637px;top:436px;color:var(--ink)">
    NEXT<svg width="7" height="10" viewBox="0 0 7 10"><path d="M1 1l4 4-4 4" fill="none" stroke="#2b2b33" stroke-width="1.3"/></svg>
  </div>

  <div class="abs rule" style="left:109px;top:524px;width:1196px"></div>

  <h3 class="abs section-title" style="left:707px;top:585px">Recently Viewed</h3>
  <div class="abs thumb" role="img" aria-label="Photo of a cured meat and cheese board" style="left:109px;top:640px;background:linear-gradient(135deg,#6b4a2c,#2c2620 60%,#1f1c1a)"></div>
  <div class="abs thumb" role="img" aria-label="Photo of rows of jam jars at a market stall" style="left:285px;top:640px;background:linear-gradient(160deg,#e9b7bf,#b8454f 55%,#7c1d24)">
    <div class="overlay"><i><svg width="12" height="11" viewBox="0 0 24 22"><path d="M12 21 2.5 11.5A5.5 5.5 0 0 1 12 4a5.5 5.5 0 0 1 9.5 7.5Z" fill="#fff"/></svg></i>Take a look</div>
  </div>
  <div class="abs thumb" role="img" aria-label="Photo of lattice berry pies on a white table" style="left:461px;top:640px;background:linear-gradient(135deg,#f2efec,#d9c9c6 50%,#eeeae6)"></div>
  <div class="abs thumb" role="img" aria-label="Photo of a market vendor with jars of honey" style="left:636px;top:640px;background:linear-gradient(180deg,#d8d6d2,#c9b8a6 55%,#8f5c35)"></div>
  <div class="abs thumb" role="img" aria-label="Photo of a pan of vegetable paella" style="left:812px;top:640px;background:radial-gradient(circle at 50% 45%,#e48a2c,#c4561d 55%,#1b3f66 80%)"></div>
  <div class="abs thumb" role="img" aria-label="Photo of a cured meat and cheese board" style="left:988px;top:640px;background:linear-gradient(135deg,#6b4a2c,#2c2620 60%,#1f1c1a)"></div>
  <div class="abs thumb" role="img" aria-label="Photo of rows of red jam jars" style="left:1164px;top:640px;width:141px;background:linear-gradient(160deg,#e6a7ad,#b62f38 55%,#6e1117)"></div>

  <div class="abs rule" style="left:113px;top:845px;width:1196px"></div>

  <footer class="abs footer">
    <div class="abs col" style="left:138px;top:54px">
      <h4>CONTACT US</h4>
      <ul><li>Tel: 1-800 555 0142</li></ul>
      <p>Monday to Friday from <b>8.30 am to 7.30 pm EST</b><br>Saturday from <b>10.00 am to 4.00 pm EST</b></p>
      <p style="margin-top:17px;color:var(--footer-text);line-height:17px;font-size:9px">contact@brindlecove.com<br>infobrindlecove@sales.com</p>
    </div>
    <div class="abs col" style="left:400px;top:54px">
      <h4>ABOUT US</h4>
      <ul><li>About</li><li>Our Story</li><li>Services</li><li>Gift Cards</li></ul>
    </div>
    <div class="abs col" style="left:544px;top:54px">
      <h4>OUR OFFERS</h4>
      <ul><li>Delivery</li><li>Sales</li><li>Gift Cards</li><li>Affiliate</li></ul>
    </div>
    <div class="abs col" style="left:687px;top:54px">
      <h4>SHIPPING INFO</h4>
      <ul><li>Returns</li><li>Shipping</li><li>Taxes</li><li>Delivery</li><li>Contact</li></ul>
    </div>
    <div class="abs col" style="left:836px;top:54px">
      <h4>SOCIAL</h4>
      <ul><li>News</li><li>Gallery</li><li>Blog</li><li>Media</li></ul>
    </div>
    <div class="abs col" style="left:1015px;top:54px">
      <h4>NEWSLETTER</h4>
      <p style="color:var(--footer-text)">Sign up to our newsletter to get the latest news.</p>
    </div>
    <div class="abs newsletter-box" style="left:1015px;top:116px">
      Subscribe to our Newsletter
      <svg width="16" height="14" viewBox="0 0 16 14"><path d="M1 1l14 6-14 6 3-6z" fill="none" stroke="#7d8089" stroke-width="1.2"/></svg>
    </div>

    <div class="abs" style="left:131px;top:203px;width:1137px;height:1px;background:#d8d9dd"></div>

    <div class="abs payments">
      <span class="pay"><i></i>Northpay</span>
      <span class="pay"><i></i>Cardwell</span>
      <span class="pay"><i></i>Tallyfund</span>
      <span class="pay"><i></i>Quillbank</span>
    </div>

    <div class="abs social" style="left:616px;top:348px" aria-label="Social link"></div>
    <div class="abs social active" style="left:660px;top:348px" aria-label="Social link"></div>
    <div class="abs social" style="left:704px;top:348px" aria-label="Social link"></div>
    <div class="abs social" style="left:748px;top:348px" aria-label="Social link"></div>
    <div class="abs social" style="left:792px;top:348px" aria-label="Social link"></div>

    <div class="abs brand" style="left:707px;top:416px">Brindlecove</div>
  </footer>
</div>
</body>
</html>
```